Corvane Communications ISP Flyer

Our company is Corvane Communications. We need to create a flyer to market our Internet/Phone services to a retirement community. We will be offering 50x50 internet connection along with a single phone line for $49.99 (before taxes). We would like to emphasize that our services are over fiber optic cables.

Internet Service
- 50x50 megabit fiber internet connection
- up to 5 email addresses
- 10gb of online storage

Phone Service
- Local 956 Phone number
- Unlimited Local/Long distance
- Caller Id
- Web access to Voicemail

Target Market(s)

Residential Customers

Industry/Entity Type

Internet

Requirements
Must have
• Company Name - Corvane Communications
Service detail

Contact info -

sales@corvaneco.example
956-483-2619

```html
<!DOCTYPE html>
<html lang="en">
<head>
<meta charset="utf-8">
<title>Corvane Communications – Internet &amp; Phone Flyer</title>
<link href="https://fonts.googleapis.com/css2?family=Archivo+Black&family=Arimo:wght@400;700&display=swap" rel="stylesheet">
<style>
  :root {
    --backdrop: #8a8a8a;
    --paper: #ffffff;
    --orange: #f0901a;
    --gold: #f6b515;
    --gold-light: #fbd98a;
    --brown: #4a2812;
    --ink: #111111;
    --card: #ececec;
    --card-edge: #e07d10;
  }
  * { box-sizing: border-box; margin: 0; padding: 0; }
  html, body { width: 1200px; height: 900px; overflow: hidden; }
  body {
    background: var(--backdrop);
    font-family: "Arimo", Arial, sans-serif;
    color: var(--ink);
    position: relative;
  }
  .flyer {
    position: absolute;
    left: 300px; top: 26px;
    width: 600px; height: 848px;
    background: var(--paper);
    overflow: hidden;
    box-shadow: 0 6px 20px rgba(0,0,0,.3);
  }
  .flyer-art { position: absolute; inset: 0; }
  .brand-title {
    position: absolute; left: 70px; top: 34px;
    font-family: "Archivo Black", Arial, sans-serif;
    font-size: 27px; letter-spacing: .2px; color: var(--ink);
  }
  .price-bubble {
    position: absolute; left: 52px; top: 84px;
    width: 164px; text-align: center; color: #fff; line-height: 1.1;
  }
  .price-bubble .lead, .price-bubble .note { font-size: 13px; }
  .price-bubble .amount { font-size: 27px; font-weight: 700; }
  .service-card {
    position: absolute; left: 0;
    width: 284px;
    padding: 14px 12px 0 46px;
    font-size: 12.5px; line-height: 1.6;
    white-space: nowrap;
  }
  .service-card h2 { font-size: 15px; font-weight: 700; line-height: 1.3; }
  .service-card.internet { top: 188px; }
  .service-card.phone { top: 332px; padding-left: 40px; font-size: 14px; line-height: 1.45; }
  .photo-label {
    position: absolute;
    font-family: "Archivo Black", Arial, sans-serif;
    font-size: 16px; color: var(--ink);
  }
  .address {
    position: absolute; left: 46px; top: 690px;
    display: flex; gap: 10px; align-items: flex-start;
    font-size: 11.5px; font-weight: 700; line-height: 1.35;
  }
  .contact-list {
    position: absolute; list-style: none;
    font-size: 11.5px; letter-spacing: .6px; line-height: 1.7;
  }
  .contact-list li { display: flex; align-items: center; gap: 10px; }
  .contact-list svg { flex: none; }
  .contact-list.online { left: 300px; top: 728px; }
  .contact-list.phones { left: 470px; top: 790px; font-size: 11px; letter-spacing: 0; }
</style>
</head>
<body>
<main class="flyer">
  <svg class="flyer-art" width="600" height="848" viewBox="0 0 600 848" aria-hidden="true">
    <defs>
      <linearGradient id="bandGrad" x1="0" y1="0" x2="1" y2="1">
        <stop offset="0" stop-color="var(--orange)"/>
        <stop offset=".45" stop-color="var(--gold)"/>
        <stop offset="1" stop-color="var(--orange)"/>
      </linearGradient>
    </defs>
    <path d="M0,95 C160,70 300,190 600,110 L600,720 C420,740 260,610 0,590 Z" fill="url(#bandGrad)"/>
    <path d="M280,140 C420,170 520,130 600,95 L600,128 C500,170 400,180 280,140 Z" fill="var(--gold-light)" opacity=".8"/>
    <ellipse cx="134" cy="122" rx="84" ry="44" fill="var(--brown)"/>
    <path d="M140,160 L156,196 L164,158 Z" fill="var(--brown)"/>
    <rect x="-20" y="188" width="304" height="118" rx="14" fill="var(--card-edge)" transform="translate(6,8)"/>
    <rect x="-20" y="188" width="304" height="118" rx="14" fill="var(--card)"/>
    <rect x="-20" y="332" width="304" height="122" rx="14" fill="var(--card-edge)" transform="translate(6,8)"/>
    <rect x="-20" y="332" width="304" height="122" rx="14" fill="var(--card)"/>
    <g fill="var(--brown)">
      <circle cx="506" cy="236" r="82"/>
      <circle cx="496" cy="398" r="82"/>
      <circle cx="484" cy="564" r="82"/>
    </g>
    <path d="M0,600 C180,560 360,740 600,700 L600,848 L0,848 Z" fill="var(--paper)"/>
  </svg>

  <svg class="flyer-art" width="600" height="848" viewBox="0 0 600 848">
    <defs>
      <radialGradient id="photoHardware" cx=".5" cy=".45" r=".6">
        <stop offset="0" stop-color="#7d8a7a"/><stop offset="1" stop-color="#e9e9e9"/>
      </radialGradient>
      <radialGradient id="photoKeypad" cx=".4" cy=".4" r=".7">
        <stop offset="0" stop-color="#8b8b8b"/><stop offset="1" stop-color="#3d3d3d"/>
      </radialGradient>
      <radialGradient id="photoPhone" cx=".45" cy=".5" r=".6">
        <stop offset="0" stop-color="#3f5d6b"/><stop offset=".6" stop-color="#c69a7a"/><stop offset="1" stop-color="#f1f1f1"/>
      </radialGradient>
    </defs>
    <circle cx="512" cy="230" r="70" fill="url(#photoHardware)" role="img" aria-label="Photo of fiber network switch hardware and circuit boards"/>
    <circle cx="502" cy="392" r="70" fill="url(#photoKeypad)" role="img" aria-label="Close-up photo of a desk phone keypad with voicemail button"/>
    <circle cx="490" cy="558" r="70" fill="url(#photoPhone)" role="img" aria-label="Photo of a hand holding a smartphone"/>
  </svg>

  <h1 class="brand-title">Corvane Communications</h1>

  <div class="price-bubble">
    <p class="lead">Phone Line For</p>
    <p class="amount">$49.99</p>
    <p class="note">(Before Taxes).</p>
  </div>

  <section class="service-card internet">
    <h2>Internet Service</h2>
    <p>50x50 megabit fiber internet connection</p>
    <p>up to 5 email addresses</p>
    <p>10gb of online storage</p>
  </section>

  <section class="service-card phone">
    <h2>Phone Service</h2>
    <p>Local 956 Phone number</p>
    <p>Unlimited Local/Long distance</p>
    <p>Caller Id</p>
    <p>Web access to Voicemail</p>
  </section>

  <span class="photo-label" style="left:336px;top:210px;">Picture-1</span>
  <span class="photo-label" style="left:322px;top:370px;">Picture-2</span>
  <span class="photo-label" style="left:306px;top:534px;">Picture-3</span>

  <div class="address">
    <svg width="22" height="20" viewBox="0 0 22 20" aria-hidden="true">
      <path d="M1,10 L11,1 L21,10 L18,10 L18,19 L4,19 L4,10 Z" fill="#b42222"/>
      <rect x="9" y="12" width="4" height="7" fill="#fff"/>
    </svg>
    <p>Address: Street/Road Name/No<br>Post Code City, Country &nbsp;Put Here</p>
  </div>

  <ul class="contact-list online">
    <li><svg width="10" height="10" viewBox="0 0 10 10" aria-hidden="true"><circle cx="5" cy="5" r="5" fill="var(--orange)"/><rect x="2.5" y="3.2" width="5" height="3.6" fill="#fff"/></svg>sales@corvaneco.example</li>
    <li><svg width="10" height="10" viewBox="0 0 10 10" aria-hidden="true"><circle cx="5" cy="5" r="5" fill="var(--orange)"/><circle cx="5" cy="5" r="2.6" fill="none" stroke="#fff"/></svg>www.corvaneco.example</li>
  </ul>

  <ul class="contact-list phones">
    <li><svg width="10" height="10" viewBox="0 0 10 10" aria-hidden="true"><circle cx="5" cy="5" r="5" fill="var(--orange)"/><path d="M3,2.5 L4.2,2.5 L4.6,4 L3.9,4.6 Q4.7,6 5.6,6.4 L6.2,5.7 L7.6,6.1 L7.6,7.3 Q4,7.6 3,2.5 Z" fill="#fff"/></svg>956-483-2619</li>
    <li><svg width="10" height="10" viewBox="0 0 10 10" aria-hidden="true"><circle cx="5" cy="5" r="5" fill="var(--orange)"/><rect x="3" y="2" width="4" height="6" rx="1" fill="#fff"/></svg>956-483-2700</li>
  </ul>
</main>
</body>
</html>
```